Lantern

My company name is lantern. The logo is attached. I am the business owner.
Name Gordon Pileck
Phone number- 2018347265
email- Gordon_pileck@mailbrook.net
Website is not live yet but it will be workwithlantern.com
the current beta link is- https://site.qvbtstage.com/lantern-v3/
on the back write “ find creative pros”
Use that beta link as reference for typography and colors on card.

```html
<!DOCTYPE html>
<html lang="en">
<head>
<meta charset="UTF-8">
<title>Lantern — Business Card</title>
<link href="https://fonts.googleapis.com/css2?family=Montserrat:wght@400;500;700;800&display=swap" rel="stylesheet">
<style>
  :root {
    --backdrop: #d3d6d7;
    --card: #141414;
    --brand-blue: #2ba6d2;
    --text-light: #d9d9d9;
    --text-muted: #a8a8a8;
    --rule: #8c8c8c;
  }
  * { box-sizing: border-box; margin: 0; padding: 0; }
  html, body {
    width: 1200px;
    height: 1050px;
    overflow: hidden;
    background: var(--backdrop);
    font-family: "Montserrat", sans-serif;
  }
  .canvas {
    width: 1200px;
    height: 1050px;
    display: flex;
    flex-direction: column;
    align-items: center;
    justify-content: center;
    gap: 70px;
  }
  .card {
    position: relative;
    width: 700px;
    height: 400px;
    background: var(--card);
    border-radius: 4px;
    box-shadow: 0 10px 28px rgba(0,0,0,0.22);
    overflow: hidden;
  }

  /* Contact side */
  .card-front .wordmark {
    position: absolute;
    top: 44px;
    right: 52px;
    font-weight: 800;
    font-size: 58px;
    letter-spacing: 1px;
    color: var(--brand-blue);
  }
  .identity {
    position: absolute;
    left: 52px;
    top: 150px;
  }
  .identity .name {
    font-weight: 700;
    font-size: 24px;
    letter-spacing: 0.5px;
    text-transform: uppercase;
    color: var(--brand-blue);
  }
  .identity .role {
    margin-top: 2px;
    font-weight: 500;
    font-size: 17px;
    color: var(--text-muted);
  }
  .divider {
    position: absolute;
    left: 140px;
    right: 52px;
    top: 205px;
    height: 1px;
    background: var(--rule);
  }
  .contact-list {
    position: absolute;
    left: 52px;
    top: 226px;
    list-style: none;
  }
  .contact-list li {
    display: flex;
    align-items: center;
    gap: 10px;
    font-size: 16px;
    font-weight: 500;
    color: var(--text-light);
    line-height: 30px;
  }
  .contact-list svg { width: 17px; height: 17px; flex: none; }
  .social {
    position: absolute;
    right: 52px;
    bottom: 44px;
    text-align: right;
  }
  .social .dots {
    display: flex;
    justify-content: flex-end;
    gap: 6px;
    margin-bottom: 8px;
  }
  .social .dot {
    width: 18px;
    height: 18px;
    border-radius: 50%;
    background: var(--brand-blue);
  }
  .social .handle {
    font-size: 18px;
    font-weight: 500;
    color: var(--text-light);
  }

  /* Brand side */
  .card-back {
    display: flex;
    flex-direction: column;
    align-items: center;
    justify-content: center;
    gap: 22px;
  }
  .card-back .wordmark {
    font-weight: 800;
    font-size: 92px;
    letter-spacing: 2px;
    color: var(--brand-blue);
    line-height: 1;
  }
  .card-back .tagline {
    font-weight: 500;
    font-size: 17px;
    letter-spacing: 5px;
    text-transform: uppercase;
    color: var(--text-light);
  }
</style>
</head>
<body>
<main class="canvas">

  <section class="card card-front" aria-label="Business card, contact side">
    <div class="wordmark">LANTERN</div>

    <div class="identity">
      <div class="name">Gordon Pileck</div>
      <div class="role">Owner</div>
    </div>

    <div class="divider"></div>

    <ul class="contact-list">
      <li>
        <svg viewBox="0 0 24 24" aria-hidden="true"><path fill="var(--brand-blue)" d="M6.6 10.8a15.1 15.1 0 0 0 6.6 6.6l2.2-2.2a1 1 0 0 1 1-.25 11.4 11.4 0 0 0 3.6.57 1 1 0 0 1 1 1V20a1 1 0 0 1-1 1A17 17 0 0 1 3 4a1 1 0 0 1 1-1h3.5a1 1 0 0 1 1 1c0 1.25.2 2.45.57 3.57a1 1 0 0 1-.25 1z"/></svg>
        2018347265
      </li>
      <li>
        <svg viewBox="0 0 24 24" aria-hidden="true"><rect x="2" y="5" width="20" height="14" rx="1.5" fill="var(--brand-blue)"/><path d="M3 6.5l9 6.5 9-6.5" fill="none" stroke="var(--card)" stroke-width="1.6"/></svg>
        Gordon_pileck@mailbrook.net
      </li>
      <li>
        <svg viewBox="0 0 24 24" aria-hidden="true"><circle cx="12" cy="12" r="9.5" fill="none" stroke="var(--brand-blue)" stroke-width="2"/><path d="M2.5 12h19M12 2.5c3 3 3 16 0 19M12 2.5c-3 3-3 16 0 19" fill="none" stroke="var(--brand-blue)" stroke-width="1.6"/></svg>
        www.workwithlantern.com
      </li>
    </ul>

    <div class="social">
      <div class="dots" aria-hidden="true">
        <span class="dot"></span><span class="dot"></span><span class="dot"></span>
      </div>
      <div class="handle">@workwithlantern</div>
    </div>
  </section>

  <section class="card card-back" aria-label="Business card, brand side">
    <div class="wordmark">LANTERN</div>
    <div class="tagline">Find creative pros</div>
  </section>

</main>
</body>
</html>
```